Sam Greenfield Billboard

**Task Description: Billboard Design for Self Storage Facility**

**Objective:**
Design a captivating billboard to promote our self-storage facility with a focus on our convenient location and online rental capabilities.

**Key Messages to Include:**
1. **Location Emphasis:** Highlight that our facility is located right beside the billboard (maybe by using an arrow pointing left).
2. **Online Rental Convenience:** Feature prominently that customers can "Rent Online Anytime!” or that we are "Always Open Online!"

**Target Audience:**
- Local residents looking for convenient self-storage solutions.
- Businesses needing storage space accessible around the clock.

**Design Elements:**
1. **Visual Impact:** Eye-catching graphics and colors that stand out against the surroundings.
2. **Clear Text:** Bold and concise messaging that can be read and understood quickly.
3. **Contact Information:** Include our phone number and website URL for easy access to further information.

**Additional Information:**
- Billboard dimensions: 12 ft. x 24 ft.
- Preferred color scheme: Bright and attention-grabbing, but professional.
- Branding: Incorporate our logo and brand colors to maintain consistency.

**Deliverables:**
- High-resolution digital file compatible with billboard printing specifications.
- Consider mockups or visualizations for presentation purposes.

Please note that I have attached current logos/graphics that we would love to incorporate into the billboard as well as a picture of our current billboard. Our logo (Sam Greenfield Self Storage - SG navy.png) MUST be incorporated into the billboard. Also feel free to add any of the current descriptions from the picture of our current billboard into the design. Instead of using "Climate Controlled" use "Temperature Controlled". Thank you for your attention to these details. We look forward to reviewing your proposed design!

```html
<!DOCTYPE html>
<html lang="en">
<head>
<meta charset="utf-8">
<title>Sam Greenfield Self Storage Billboard</title>
<link rel="stylesheet" href="https://fonts.googleapis.com/css2?family=Barlow+Semi+Condensed:wght@700;800&family=Poppins:wght@700&display=swap">
<style>
  :root {
    --stage: #555555;
    --paper: #ffffff;
    --navy: #0d2a5c;
    --band-blue: #13306a;
    --signal-red: #c8202a;
    --ink: #222222;
    --kraft: #a88a66;
    --kraft-dark: #8f7352;
    --device: #2b2f38;
  }
  * { margin: 0; padding: 0; box-sizing: border-box; }
  html, body { width: 831px; height: 1200px; overflow: hidden; }
  body { background: var(--stage); position: relative; }

  .billboard {
    position: absolute; left: 20px; top: 402px;
    width: 791px; height: 395px;
    background: var(--paper); overflow: hidden;
  }
  .feature-panel {
    position: absolute; left: 428px; top: 0; width: 363px; height: 275px;
    background: linear-gradient(90deg, var(--kraft) 0%, var(--kraft-dark) 50%, var(--kraft) 100%);
  }
  .brand {
    position: absolute; left: 39px; top: 42px;
    display: flex; align-items: center; gap: 10px;
    font-family: "Barlow Semi Condensed", sans-serif; font-weight: 800;
    color: var(--navy); line-height: 0.95;
  }
  .brand-dot { width: 34px; height: 34px; border-radius: 50%; background: var(--navy); flex: none; }
  .brand-name { font-size: 34px; letter-spacing: 0.5px; }
  .brand-name span { display: block; font-size: 20px; letter-spacing: 5px; margin-top: 4px; }

  .headline {
    position: absolute; left: 38px; top: 124px;
    font-family: "Barlow Semi Condensed", sans-serif; font-weight: 800;
    font-size: 66px; line-height: 0.9; color: var(--navy); letter-spacing: -0.5px;
  }

  .features {
    position: absolute; left: 448px; top: 34px; list-style: none;
    font-family: "Barlow Semi Condensed", sans-serif; font-weight: 800;
    font-size: 22px; color: var(--paper); line-height: 35px;
  }
  .features li { display: flex; align-items: center; gap: 10px; }
  .features svg { width: 18px; height: 18px; flex: none; }

  .device-showcase {
    position: absolute; left: 455px; top: 141px; width: 285px; height: 131px;
    border-radius: 6px;
    background: linear-gradient(180deg, #3a3f4a 0%, var(--device) 100%);
  }

  .base-band { position: absolute; left: 0; top: 289px; width: 791px; height: 106px; background: var(--ink); }
  .arrow-head { position: absolute; left: 24px; top: 267px; width: 40px; height: 58px; }
  .address-bar {
    position: absolute; left: 63px; top: 275px; width: 350px; height: 44px;
    background: var(--signal-red); color: var(--paper);
    display: flex; align-items: center; gap: 8px; padding-left: 14px;
    font-family: "Barlow Semi Condensed", sans-serif; font-weight: 700; font-size: 34px;
  }
  .address-bar svg, .phone-bar svg { width: 22px; height: 22px; flex: none; }
  .phone-bar {
    position: absolute; left: 413px; top: 275px; width: 378px; height: 44px;
    background: var(--band-blue); color: var(--paper);
    display: flex; align-items: center; gap: 10px; padding-left: 16px;
    font-family: "Poppins", sans-serif; font-weight: 700; font-size: 31px;
  }
  .web-address {
    position: absolute; left: 0; top: 324px; width: 791px; text-align: center;
    font-family: "Poppins", sans-serif; font-weight: 700; font-size: 40px;
    color: var(--paper); line-height: 60px;
  }
</style>
</head>
<body>
  <section class="billboard">
    <div class="feature-panel"></div>

    <div class="brand">
      <div class="brand-dot"></div>
      <div class="brand-name">SAM GREENFIELD<span>SELF STORAGE</span></div>
    </div>

    <h1 class="headline">RENT ONLINE<br>ANYTIME!</h1>

    <ul class="features">
      <li><svg viewBox="0 0 20 20"><circle cx="10" cy="10" r="10" fill="#0d2a5c"/><path d="M5.5 10.5l3 3 6-6.5" stroke="#fff" stroke-width="2.2" fill="none" stroke-linecap="round" stroke-linejoin="round"/></svg>LARGE/ SMALL UNITS</li>
      <li><svg viewBox="0 0 20 20"><circle cx="10" cy="10" r="10" fill="#0d2a5c"/><path d="M5.5 10.5l3 3 6-6.5" stroke="#fff" stroke-width="2.2" fill="none" stroke-linecap="round" stroke-linejoin="round"/></svg>TEMPERATURE CONTROLLED</li>
      <li><svg viewBox="0 0 20 20"><circle cx="10" cy="10" r="10" fill="#0d2a5c"/><path d="M5.5 10.5l3 3 6-6.5" stroke="#fff" stroke-width="2.2" fill="none" stroke-linecap="round" stroke-linejoin="round"/></svg>COVERED BOAT/RV PARKING</li>
    </ul>

    <div class="device-showcase" role="img" aria-label="Tablet, laptop and phone showing the online rental website"></div>

    <div class="base-band"></div>

    <svg class="arrow-head" viewBox="0 0 40 58"><polygon points="0,29 40,0 40,58" fill="#c8202a"/></svg>
    <div class="address-bar">
      <svg viewBox="0 0 24 24"><path d="M12 2a7 7 0 0 0-7 7c0 5.3 7 13 7 13s7-7.7 7-13a7 7 0 0 0-7-7z" fill="#fff"/><circle cx="12" cy="9" r="2.6" fill="#c8202a"/></svg>
      248 OAKHAVEN DRIVE
    </div>
    <div class="phone-bar">
      <svg viewBox="0 0 24 24"><path d="M6.6 10.8a15 15 0 0 0 6.6 6.6l2.2-2.2a1 1 0 0 1 1-.25 11.4 11.4 0 0 0 3.6.57 1 1 0 0 1 1 1V20a1 1 0 0 1-1 1A17 17 0 0 1 3 4a1 1 0 0 1 1-1h3.5a1 1 0 0 1 1 1c0 1.25.2 2.45.57 3.57a1 1 0 0 1-.25 1z" fill="#fff"/></svg>
      478-555-0142
    </div>
    <div class="web-address">SamGreenfieldStorage.com</div>
  </section>
</body>
</html>
```